Elegant sophisticated Invitation Design in A5

"Amber Hours of Vellmoor"
We are after an invitation A5 portrait size. It is for an outdoor event for a 4 course dinner. It needs to display high class, elegance and sophistication. We like the idea of having stars or reflections on the water (as per attached images we found on findora)

Text and logo are attached. The file needs to be supplied to use as psd file and needs to be 300dpi at least as the invitation will be printed.

We would like dark colours, black, and sparkles/stars.

The main focus is elegance!

Logos and text are attached.

Target Market(s)

Upper class, business men and women, Suit and tie event

Industry/Entity Type

Event

Font styles to use
Decorative
Script

Colors
fffefe
000000

Requirements
Must have
• The element of Water and stars or sparkles. It needs to speak elegance throughout. The fonts chosen need to be soft and elegant. The logo attached must be used either with the diamond or the standard version a mono version can also be used. Open for designers ideas.
Should not have
• Bold and bulky fonts it needs to be soft

```html
<!DOCTYPE html>
<html lang="en">
<head>
<meta charset="utf-8">
<title>Amber Hours of Vellmoor – VIP Dinner Invitation</title>
<link href="https://fonts.googleapis.com/css2?family=Great+Vibes&family=Oswald:wght@400;500&family=Hind:wght@400;500&display=swap" rel="stylesheet">
<style>
  :root {
    --ink: #000000;
    --night: #0b0f10;
    --deep-teal: #17302f;
    --water: #3f6764;
    --shimmer: #9fb8b6;
    --teal: #2fc6c9;
    --gold: #d6b45e;
    --gold-light: #f4dd97;
    --silver: #e4e8ea;
    --white: #fffefe;
  }
  * { margin: 0; padding: 0; box-sizing: border-box; }
  html, body { width: 931px; height: 1200px; overflow: hidden; background: #1a1c1d; }
  .invitation {
    position: relative;
    width: 931px; height: 1200px;
    background: var(--ink);
    overflow: hidden;
    font-family: 'Hind', sans-serif;
    color: var(--white);
    text-align: center;
  }
  .sky-glow {
    position: absolute; left: 0; right: 0; top: 0; height: 260px;
    background:
      radial-gradient(ellipse 30% 45% at 30% 30%, rgba(140,170,140,.35), transparent 70%),
      radial-gradient(ellipse 30% 45% at 75% 25%, rgba(150,160,120,.30), transparent 70%),
      radial-gradient(ellipse 45% 60% at 50% 10%, rgba(70,110,100,.45), transparent 75%),
      linear-gradient(180deg, #1c2a27 0%, #0e1514 100%);
  }
  .hills { position: absolute; left: 0; top: 150px; }
  .water {
    position: absolute; left: 0; right: 0; top: 205px; bottom: 0;
    background:
      radial-gradient(ellipse 14% 34% at 50% 36%, rgba(170,205,200,.35), transparent 75%),
      radial-gradient(ellipse 60% 20% at 45% 78%, rgba(159,184,182,.32), transparent 75%),
      radial-gradient(ellipse 40% 14% at 60% 92%, rgba(159,184,182,.22), transparent 75%),
      radial-gradient(ellipse 35% 10% at 30% 66%, rgba(63,103,100,.45), transparent 75%),
      linear-gradient(180deg, #0a0f0f 0%, #0e1616 40%, #142020 70%, #070a0a 100%);
  }
  .frame {
    position: absolute; left: 38px; top: 30px; right: 38px; bottom: 30px;
    border: 1.5px solid rgba(200,210,210,.28);
  }
  .arc { position: absolute; left: 0; top: 0; }
  .brand {
    position: absolute; top: 120px; left: 0; right: 0;
    display: flex; flex-direction: column; align-items: center; gap: 4px;
  }
  .brand-mark { width: 14px; height: 14px; border-radius: 50%; background: var(--silver); }
  .brand-name { font-weight: 500; font-size: 24px; color: var(--white); }
  .brand-tag { font-size: 16px; font-weight: 500; letter-spacing: 1px; color: var(--white); }
  .kicker {
    position: absolute; top: 278px; left: 0; right: 0;
    font-family: 'Oswald', sans-serif; font-size: 20px; letter-spacing: .5px; color: var(--teal);
  }
  .title { position: absolute; top: 306px; left: 0; right: 0; font-family: 'Great Vibes', cursive; font-weight: 400; }
  .title-gold {
    display: block; font-size: 112px; line-height: 1.3; padding-top: 6px;
    background: linear-gradient(180deg, var(--gold-light), var(--gold) 55%, #8f6f2c);
    -webkit-background-clip: text; background-clip: text; color: transparent;
  }
  .title-line2 { display: block; margin-top: -22px; line-height: 1.3; }
  .title-small { font-size: 56px; color: var(--white); margin-right: 14px; }
  .title-silver {
    font-size: 118px; padding: 0 12px;
    background: linear-gradient(180deg, #ffffff, #c9ced1 60%, #8e9599);
    -webkit-background-clip: text; background-clip: text; color: transparent;
  }
  .rule { position: absolute; left: 350px; width: 231px; height: 1px; background: linear-gradient(90deg, transparent, var(--gold), transparent); }
  .event { position: absolute; top: 630px; left: 0; right: 0; font-family: 'Oswald', sans-serif; line-height: 1; }
  .event-label { font-size: 30px; letter-spacing: 14px; color: var(--white); opacity: .9; }
  .event-name { font-size: 58px; font-weight: 500; letter-spacing: 4px; color: var(--white); margin-top: 6px; }
  .event-date { font-size: 30px; color: var(--gold-light); margin-top: 8px; }
  .venue { position: absolute; top: 790px; left: 0; right: 0; font-family: 'Oswald', sans-serif; line-height: 1.1; }
  .venue-name { font-size: 34px; font-weight: 500; color: var(--gold); }
  .venue-address { font-size: 24px; color: var(--white); }
  .mission { position: absolute; top: 878px; left: 0; right: 0; font-size: 18px; letter-spacing: 1.2px; line-height: 1.35; }
  .access { position: absolute; top: 948px; left: 0; right: 0; font-family: 'Oswald', sans-serif; font-size: 19px; color: var(--gold-light); }
  .stars { position: absolute; top: 985px; left: 0; right: 0; display: flex; justify-content: center; gap: 14px; }
  .stars svg { width: 16px; height: 16px; fill: var(--gold-light); }
  .details { position: absolute; top: 1022px; left: 0; right: 0; font-size: 18px; line-height: 1.75; }
</style>
</head>
<body>
<main class="invitation">
  <div class="sky-glow" role="img" aria-label="Soft bokeh of coloured lights in the night sky above distant hills"></div>
  <svg class="hills" width="931" height="70" aria-hidden="true">
    <path d="M0 40 C120 30 200 20 300 38 C380 52 460 30 560 34 C680 40 760 20 931 36 L931 70 L0 70 Z" fill="#0a0e0e"/>
  </svg>
  <div class="water" role="img" aria-label="Dark water at night with a moonlit reflection and sparkling star-like glints on the surface"></div>
  <svg class="arc" width="931" height="1200" aria-hidden="true">
    <path d="M300 720 A215 215 0 1 1 632 720" fill="none" stroke="rgba(180,200,200,.14)" stroke-width="3"/>
  </svg>
  <div class="frame"></div>

  <header class="brand">
    <span class="brand-mark"></span>
    <span class="brand-name">Harrowgate Northern Region</span>
    <span class="brand-tag">Access for All</span>
  </header>

  <p class="kicker">HARROWGATE NORTHERN REGION'S &nbsp;INAUGURAL</p>

  <h1 class="title">
    <span class="title-gold">Amber Hours</span>
    <span class="title-line2"><span class="title-small">of</span><span class="title-silver">Vellmoor</span></span>
  </h1>

  <div class="rule" style="top:620px"></div>
  <section class="event">
    <p class="event-label">VIP DINNER</p>
    <p class="event-name">LE BANQUET</p>
    <p class="event-date">SATURDAY 17TH JULY 2017</p>
  </section>
  <div class="rule" style="top:772px"></div>

  <section class="venue">
    <p class="venue-name">HARBOURLINE HERITAGE PARK</p>
    <p class="venue-address">CARROW STREET, SOUTH FERRISPORT</p>
  </section>

  <p class="mission">BUILDING ACCESSIBLE HOUSING FOR PEOPLE WITH DISABILITY<br>IN THE NORTHERN REGION</p>

  <p class="access">BY INVITATION</p>

  <div class="stars" aria-hidden="true">
    <svg viewBox="0 0 24 24"><path d="M12 2l3 7 7 .6-5.4 4.7 1.7 7.2L12 17.8 5.7 21.5l1.7-7.2L2 9.6 9 9z"/></svg>
    <svg viewBox="0 0 24 24"><path d="M12 2l3 7 7 .6-5.4 4.7 1.7 7.2L12 17.8 5.7 21.5l1.7-7.2L2 9.6 9 9z"/></svg>
    <svg viewBox="0 0 24 24"><path d="M12 2l3 7 7 .6-5.4 4.7 1.7 7.2L12 17.8 5.7 21.5l1.7-7.2L2 9.6 9 9z"/></svg>
    <svg viewBox="0 0 24 24"><path d="M12 2l3 7 7 .6-5.4 4.7 1.7 7.2L12 17.8 5.7 21.5l1.7-7.2L2 9.6 9 9z"/></svg>
    <svg viewBox="0 0 24 24"><path d="M12 2l3 7 7 .6-5.4 4.7 1.7 7.2L12 17.8 5.7 21.5l1.7-7.2L2 9.6 9 9z"/></svg>
    <svg viewBox="0 0 24 24"><path d="M12 2l3 7 7 .6-5.4 4.7 1.7 7.2L12 17.8 5.7 21.5l1.7-7.2L2 9.6 9 9z"/></svg>
  </div>

  <section class="details">
    <p>Four course dinner exclusively crafted by The Brinewell Kitchen</p>
    <p>Beautiful wines and fine beers included</p>
    <p>Live Entertainment</p>
  </section>
</main>
</body>
</html>
```